Star Ridgeline Junior Postcard for special events

Need creative display for platform of logo for Star Ridgeline on her large postcards. Be kind, be bold, be brave, be you is the message. Please include this quote:
Kindness is the language which the deaf can hear
and the blind can see. - Hollis Brandt
Her title is 2017 Star Ridgeline National Scholar Junior. Her name is Corinne Tabor. We have pics that we want included on the card. We want it to have a front and back. You can use any combination of the photos. thanks!

Target Market(s)

Youth/ Young Adults

Industry/Entity Type

Events

Font styles to use
Sans Serif
Script

Colors
86cfc6
33b8a4
3276b5
0255a3

Requirements
Must have
• Kindness is the language which the deaf can hear
• and the blind can see. - Hollis Brandt
• Title-
• Name
• She is partial to the jumpsuit photo for the front but open to others
• Be Kind, Be Bold, Be Brave, Be you - would like this on the front
• Also please include Instgram: crtabor202 twitter: crtabor202 corinne34@brightmailbox.net
• #brightsteadytrue
Nice to have
• Anything that would inspire youth especially. Have begun events at hospitals and lining up work to assist with donations for community resources but not sure that is appropriate for this. We lean more towards the green than the blue, unless it ties with other things you see better- or a better shade.thanks
Should not have
• Should be age appropriate and appropriate for all ages.
• Postcard is for handing out / does not need to be mailed. Can seek revisions if this becomes the case

```html
<!DOCTYPE html>
<html lang="en">
<head>
<meta charset="utf-8">
<title>Star Ridgeline Junior Postcard</title>
<link href="https://fonts.googleapis.com/css2?family=Cinzel:wght@400;700&family=Poiret+One&family=Lato:wght@700&display=swap" rel="stylesheet">
<style>
  :root{
    --teal:#33b8a4;
    --teal-soft:#86cfc6;
    --ink:#1d1d1d;
    --paper:#ffffff;
    --stage:#e9eaec;
    --stamp:#6b6b6b;
    --rule:#d9dbde;
  }
  *{margin:0;padding:0;box-sizing:border-box}
  html,body{width:1200px;height:1200px;overflow:hidden;background:var(--stage)}
  .canvas{position:relative;width:1200px;height:1200px}

  .card{position:absolute;background:var(--paper);box-shadow:0 6px 18px rgba(0,0,0,.18);overflow:hidden}
  .card-front{left:69px;top:226px;width:439px;height:615px;
    background:
      radial-gradient(circle at 100% 10%, rgba(248,190,185,.55), transparent 32%),
      radial-gradient(circle at 0% 92%, rgba(249,215,200,.6), transparent 30%),
      radial-gradient(circle at 70% 100%, rgba(248,205,210,.45), transparent 28%),
      var(--paper);}
  .card-back{left:539px;top:403px;width:616px;height:439px;
    background:
      radial-gradient(circle at 12% 12%, rgba(248,205,210,.6), transparent 28%),
      radial-gradient(circle at 40% 100%, rgba(248,205,210,.55), transparent 30%),
      radial-gradient(circle at 88% 28%, rgba(225,225,228,.7), transparent 30%),
      var(--paper);}

  /* front */
  .motto{position:absolute;left:0;right:0;top:38px;text-align:center;font-family:"Poiret One",sans-serif;font-weight:400;font-size:33px;color:var(--ink);letter-spacing:-.8px;white-space:nowrap;-webkit-text-stroke:.6px var(--ink)}
  .motto-main{position:absolute;left:0;right:0;top:72px;text-align:center;font-family:"Cinzel",serif;font-weight:400;font-size:48px;color:var(--teal);letter-spacing:1px}
  .front-art{position:absolute;left:0;top:0}
  .title-rule{position:absolute;height:1px;background:var(--teal)}
  .title-year{position:absolute;left:0;right:0;top:472px;text-align:center;font-family:"Cinzel",serif;font-weight:700;font-size:25px;color:var(--ink)}
  .title-sub{position:absolute;left:0;right:0;top:503px;text-align:center;font-family:"Cinzel",serif;font-size:11.5px;letter-spacing:2.6px;color:var(--ink)}
  .name{position:absolute;left:0;right:0;top:551px;text-align:center;font-family:"Poiret One",sans-serif;font-size:33px;color:var(--teal);text-transform:uppercase;-webkit-text-stroke:.4px var(--teal)}

  /* back */
  .back-art{position:absolute;left:0;top:0}
  .quote{position:absolute;left:42px;top:42px;font-family:"Cinzel",serif;font-size:13.5px;line-height:18px;color:var(--ink)}
  .quote-mark{position:absolute;font-family:"Cinzel",serif;font-weight:700;font-size:30px;color:var(--teal);line-height:1}
  .quote-open{left:19px;top:28px}
  .quote-close{left:232px;top:78px}
  .quote-author{position:absolute;right:358px;top:105px;font-family:"Lato",sans-serif;font-weight:700;font-size:12px;color:var(--ink)}
  .stamp{position:absolute;left:517px;top:31px;width:66px;height:66px;background:var(--stamp)}
  .address-line{position:absolute;left:382px;width:192px;height:1px;background:var(--rule)}
  .contact{position:absolute;display:flex;align-items:center;gap:6px;font-family:"Cinzel",serif;font-size:11px;color:var(--ink);text-transform:uppercase}
  .contact-dot{width:14px;height:14px;border-radius:50%;background:var(--teal);flex:none}
  .hashtag{position:absolute;right:342px;top:406px;font-family:"Cinzel",serif;font-size:9.5px;color:var(--ink);text-transform:uppercase}
</style>
</head>
<body>
<main class="canvas">

  <section class="card card-front">
    <p class="motto">BE KIND | BE BOLD | BE BRAVE</p>
    <h1 class="motto-main">BE YOU</h1>
    <svg class="front-art" width="439" height="615" viewBox="0 0 439 615">
      <defs>
        <linearGradient id="front-photo-tone" x1="0" y1="0" x2="0" y2="1">
          <stop offset="0" stop-color="#9aa39a"/>
          <stop offset=".5" stop-color="#c9b3a3"/>
          <stop offset="1" stop-color="#b9745c"/>
        </linearGradient>
      </defs>
      <circle cx="224" cy="283" r="148" fill="none" stroke="var(--teal)" stroke-width="4"/>
      <circle cx="224" cy="283" r="136" fill="url(#front-photo-tone)" role="img" aria-label="Portrait photo of Corinne Tabor in a rust jumpsuit on a city street"/>
    </svg>
    <div class="title-rule" style="left:76px;width:287px;top:459px"></div>
    <p class="title-year">2017 Star Ridgeline</p>
    <p class="title-sub">NATIONAL SCHOLAR JUNIOR</p>
    <div class="title-rule" style="left:76px;width:287px;top:536px"></div>
    <p class="name">Corinne Tabor</p>
  </section>

  <section class="card card-back">
    <svg class="back-art" width="616" height="439" viewBox="0 0 616 439">
      <defs>
        <linearGradient id="back-photo-tone" x1="0" y1="0" x2="1" y2="1">
          <stop offset="0" stop-color="#f0b92a"/>
          <stop offset=".6" stop-color="#c58a5a"/>
          <stop offset="1" stop-color="#3a2a22"/>
        </linearGradient>
      </defs>
      <path d="M335 0 Q312 118 249 193" fill="none" stroke="var(--teal)" stroke-width="8"/>
      <path d="M229 297 Q300 355 328 439" fill="none" stroke="var(--teal)" stroke-width="8"/>
      <path d="M0 252 Q30 244 57 243" fill="none" stroke="var(--teal)" stroke-width="7"/>
      <circle cx="153" cy="235" r="94" fill="var(--paper)" stroke="var(--teal)" stroke-width="5"/>
      <circle cx="153" cy="235" r="86" fill="url(#back-photo-tone)" role="img" aria-label="Portrait photo of Corinne Tabor smiling against a yellow backdrop"/>
    </svg>
    <span class="quote-mark quote-open">“</span>
    <p class="quote">KINDNESS IS THE LANGUAGE<br>WHICH THE DEAF CAN HEAR<br>AND THE BLIND CAN SEE</p>
    <span class="quote-mark quote-close">”</span>
    <p class="quote-author">Hollis Brandt</p>
    <div class="stamp"></div>
    <div class="address-line" style="top:217px"></div>
    <div class="address-line" style="top:247px"></div>
    <div class="address-line" style="top:278px"></div>
    <div class="address-line" style="top:308px"></div>
    <p class="contact" style="left:30px;top:356px"><span class="contact-dot"></span>crtabor202</p>
    <p class="contact" style="left:141px;top:356px"><span class="contact-dot"></span>crtabor202</p>
    <p class="contact" style="left:30px;top:382px"><span class="contact-dot"></span>corinne34@brightmailbox.net</p>
    <p class="hashtag">#brightsteadytrue</p>
  </section>

</main>
</body>
</html>
```